Corvane Building Company Portfolio Design

I need a full design for a Company Portfolio for a Kuwait based company called Corvane Building Company, WLL. We offer services in Construction ( Supply of Construction Machinery & Construction Material), Contracting (Steel Structure, Furnishing & Finishing) and Smart Solutions (Smart Homes & Smart Parking).

https://www.filtrobay.com/s/qmtpvkadnehzwro/Photos.zip
Updates

This is a Filtro Bay Link containing all our images that can be used in the Company Profile.

One or more of each can be more than enough to describe each product or service we provide.

Target Market(s)

Construction Companies, Engineering & Design Companies, Consultancy firms.

Industry/Entity Type

Construction

Requirements
Must have
• 1) Must allow for further addition & modification.
Nice to have
• 1) External Photos can be used for a better look & resolution.

```html
<!DOCTYPE html>
<html lang="en">
<head>
<meta charset="utf-8">
<title>Corvane Building Company – Divisions</title>
<link href="https://fonts.googleapis.com/css2?family=Open+Sans:wght@400;600;800&display=swap" rel="stylesheet">
<style>
  :root {
    --bg: #2a2727;
    --bg-shade: #3a3636;
    --teal: #03777e;
    --white: #ffffff;
    --blue: #3b79c8;
    --blue-dark: #2c5fa3;
    --red: #c9393d;
    --red-dark: #a82c30;
    --green: #8fc641;
    --green-dark: #78ad2f;
    --purple: #7d50ab;
    --purple-dark: #683f93;
    --line-red: #dba2a2;
    --line-green: #c6d98f;
    --line-purple: #a98cc8;
  }
  html, body { margin: 0; padding: 0; overflow: hidden; }
  body { width: 1200px; height: 928px; background: var(--bg); }
  .page {
    position: relative; width: 1200px; height: 928px; overflow: hidden;
    background: var(--bg); font-family: "Open Sans", Arial, sans-serif;
  }
  .site-backdrop {
    position: absolute; inset: 0;
    background: linear-gradient(90deg, var(--bg-shade) 0%, var(--bg) 45%, var(--bg) 60%, var(--bg-shade) 100%);
  }
  .header-band { position: absolute; left: 0; top: 0; width: 1200px; height: 220px; }
  .header-text {
    position: absolute; left: 37px; top: 78px; width: 1140px; color: var(--white);
    transform: rotate(-2.86deg); transform-origin: 0 0;
  }
  .header-title { margin: 0 0 12px; font-size: 19px; font-weight: 800; }
  .header-intro { margin: 0; font-size: 17px; font-weight: 800; line-height: 28px; }
  .connectors { position: absolute; inset: 0; }
  .node {
    position: absolute; display: flex; align-items: center; justify-content: center;
    text-align: center; color: var(--white); font-size: 12px; line-height: 22px;
    box-shadow: 0 2px 3px rgba(0,0,0,.45); box-sizing: border-box; padding: 0 4px;
    border-top: 1px solid rgba(255,255,255,.35);
  }
  .node-root { background: linear-gradient(var(--blue), var(--blue-dark)); width: 119px; height: 62px; }
  .node-division { background: linear-gradient(var(--red), var(--red-dark)); width: 119px; height: 64px; top: 304px; }
  .node-group { background: linear-gradient(var(--green), var(--green-dark)); width: 118px; height: 62px; top: 389px; }
  .node-service { background: linear-gradient(var(--purple), var(--purple-dark)); width: 119px; height: 63px; }
</style>
</head>
<body>
<div class="page">
  <div class="site-backdrop" role="img" aria-label="Dark photo of a construction site with tower cranes and silhouetted workers"></div>

  <svg class="header-band" viewBox="0 0 1200 220" aria-hidden="true">
    <polygon points="0,66 1200,6 1200,12 0,72" fill="var(--white)"/>
    <polygon points="0,75 1200,15 1200,145 0,205" fill="var(--teal)"/>
    <polygon points="0,205 1200,145 1200,151 0,211" fill="var(--white)"/>
  </svg>
  <div class="header-text">
    <h1 class="header-title">Divisions</h1>
    <p class="header-intro">Corvane Building Company’s reputation is the foundation of everything we do. We are proud to offer services in the following:</p>
  </div>

  <svg class="connectors" width="1200" height="928" aria-hidden="true" fill="none" stroke-width="1.5">
    <g stroke="var(--line-red)">
      <line x1="589" y1="276" x2="589" y2="304"/>
      <line x1="346" y1="336" x2="829" y2="336"/>
    </g>
    <g stroke="var(--line-green)">
      <path d="M286 368V377M215 389V377H358V389"/>
      <path d="M589 368V377M516 389V377H661V389"/>
      <path d="M889 368V377M816 389V377H960V389"/>
    </g>
    <g stroke="var(--line-purple)">
      <path d="M168 451V672M168 505H186M168 588H186M168 672H186"/>
      <path d="M311 451V588M311 505H328M311 588H328"/>
      <path d="M471 451V841M471 505H487M471 588H487M471 672H487M471 757H487M471 841H487"/>
      <path d="M614 451V841M614 505H631M614 588H631M614 672H631M614 757H631M614 841H631"/>
      <path d="M770 451V672M770 505H788M770 588H788M770 672H788"/>
      <path d="M913 451V841M913 505H930M913 588H930M913 672H930M913 757H930M913 841H930"/>
    </g>
  </svg>

  <div class="node node-root" style="left:530px;top:214px">Divisions</div>

  <div class="node node-division" style="left:227px">Construction</div>
  <div class="node node-division" style="left:530px">Smart Solutions</div>
  <div class="node node-division" style="left:829px">Contracting</div>

  <div class="node node-group" style="left:156px">Construction<br>Machinery</div>
  <div class="node node-group" style="left:298px">Construction<br>Materials</div>
  <div class="node node-group" style="left:457px">Smart Homes</div>
  <div class="node node-group" style="left:602px">Smart Parking</div>
  <div class="node node-group" style="left:757px">Steel Structure</div>
  <div class="node node-group" style="left:901px">Finishing &amp;<br>Furnishing</div>

  <div class="node node-service" style="left:186px;top:474px">Tower Cranes</div>
  <div class="node node-service" style="left:186px;top:557px">Construction Hoists</div>
  <div class="node node-service" style="left:186px;top:641px">Overhead Cranes</div>

  <div class="node node-service" style="left:328px;top:474px">Concrete<br>Framework Wood</div>
  <div class="node node-service" style="left:328px;top:557px">Reinforcing Steel</div>

  <div class="node node-service" style="left:487px;top:474px">Lighting<br>Automations</div>
  <div class="node node-service" style="left:487px;top:557px">Blind/Curtain<br>Automation</div>
  <div class="node node-service" style="left:487px;top:641px">Temperature<br>Automation</div>
  <div class="node node-service" style="left:487px;top:725px">Security</div>
  <div class="node node-service" style="left:487px;top:809px">Entertainment</div>

  <div class="node node-service" style="left:631px;top:474px">Rotary Parking</div>
  <div class="node node-service" style="left:631px;top:557px">Puzzle Parking</div>
  <div class="node node-service" style="left:631px;top:641px">Tower Parking</div>
  <div class="node node-service" style="left:631px;top:725px">Stackers</div>
  <div class="node node-service" style="left:631px;top:809px">Turntables</div>

  <div class="node node-service" style="left:788px;top:474px">Structural Steel<br>Building</div>
  <div class="node node-service" style="left:788px;top:557px">Pre-Engineered<br>Buildings</div>
  <div class="node node-service" style="left:788px;top:641px">Metal Decking &amp;<br>Shear Studs</div>

  <div class="node node-service" style="left:930px;top:474px">Marble &amp; Granite</div>
  <div class="node node-service" style="left:930px;top:557px">Curtain Wall</div>
  <div class="node node-service" style="left:930px;top:641px">Wall Protection</div>
  <div class="node node-service" style="left:930px;top:725px">Hardwood Decking<br>&amp; Flooring</div>
  <div class="node node-service" style="left:930px;top:809px">Furniture</div>
</div>
</body>
</html>
```